Tarvon Letterhead

Looking for a design template for our company’s official letterheads & business cards.It has to be mainly white and include our company logo, website, social media handle, address, phone number. Visit our website to have an idea of our brand identity and colours. Please use the same font that we are using in our website.
Target Market(s)
Lubricants & Greases, Industrial markets, Automotive
Font styles to use
Other font styles liked:
- Saira Extra-Condensed
Colors
ffffff
000000
fbee3f
Requirements
Must have
- It must be consistent with our brand identity. It must use the same exact yellow (Pantone color: 102C) and black (Pantone color: K100) as our brand colors.
- Must also use our font attached (Saira.zip). It's called Saira Extra-Condensed.
- We intend to use the TARVON logo and not the small mini-TV logo.
- On the design we must include ALL of the following:
- E-mail: info@tarvonfluids.example
- @TarvonFluids
- www.tarvonfluids.example
- Address: P.O. Boc 4827, Qurain 73504, Kuwait
- Phone: (+965) 24718593
- Kuwait Morel Oils logo (attached). The logo attached is in Blue/Red but you can select one solid color for all of it such as BLACK or YELLOW depending on what background color you'll select.
Nice to have
- Like it to be as professional and as modern as possible. It has look clean, slick and classy.
Should not have
- Too many different colors.

```html
<!DOCTYPE html>
<html lang="en">
<head>
<meta charset="utf-8">
<title>Tarvon Stationery</title>
<link rel="stylesheet" href="https://fonts.googleapis.com/css2?family=Saira+Extra+Condensed:wght@400;600;700;800&family=Source+Sans+3:wght@400;600&display=swap">
<style>
  :root {
    --brand-yellow: #fbee3f;
    --brand-black: #000000;
    --paper: #ffffff;
    --backdrop: #e6e6e6;
    --ink: #1a1a1a;
    --display: "Saira Extra Condensed", "Arial Narrow", sans-serif;
    --body: "Source Sans 3", Arial, sans-serif;
  }
  * { box-sizing: border-box; margin: 0; padding: 0; }
  html, body { width: 1200px; height: 1000px; overflow: hidden; }
  body { background: var(--backdrop); position: relative; font-family: var(--body); color: var(--ink); }
  .icon-defs { position: absolute; width: 0; height: 0; }
  .wordmark { position: absolute; display: block; overflow: visible; }
  .wordmark text { font-family: var(--display); font-weight: 800; }

  /* Letterhead */
  .letterhead { position: absolute; left: 150px; top: 79px; width: 598px; height: 847px; background: var(--paper); overflow: hidden; }
  .letterhead__brand { left: 36px; top: 36px; }
  .letterhead__contact { position: absolute; right: 35px; top: 44px; list-style: none; text-align: right; font-family: var(--display); font-size: 9px; line-height: 1.05; color: var(--ink); white-space: nowrap; }
  .letterhead__contact li { display: flex; justify-content: flex-end; align-items: center; gap: 7px; margin-bottom: 5px; }
  .letterhead__contact svg { width: 11px; height: 11px; flex: none; }
  .letter__label { position: absolute; font-size: 9px; font-weight: 600; text-transform: uppercase; letter-spacing: .2px; }
  .letter__salutation { left: 38px; top: 184px; }
  .letter__signoff { right: 38px; top: 702px; }
  .letter__body { position: absolute; left: 35px; top: 250px; width: 528px; font-size: 9.4px; line-height: 11.8px; text-align: justify; }
  .letter__body p { margin-bottom: 12px; }
  .letterhead__footer { position: absolute; left: 0; bottom: 0; width: 598px; height: 54px; }

  /* Business cards */
  .card { position: absolute; left: 809px; width: 228px; height: 399px; overflow: hidden; }
  .card--front { top: 80px; background: var(--brand-yellow); }
  .card--back { top: 525px; background: var(--brand-black); }
  .card__shape { position: absolute; left: 0; top: 0; }
  .card--front .card__brand { left: 39px; top: 48px; }
  .card__person { position: absolute; left: 53px; top: 180px; font-family: var(--display); color: var(--brand-yellow); line-height: 1; white-space: nowrap; }
  .card__name { font-weight: 700; font-size: 15px; letter-spacing: .5px; }
  .card__role { font-size: 13px; margin-top: 1px; }
  .card__contact { position: absolute; left: 19px; top: 246px; list-style: none; font-family: var(--display); font-size: 12px; line-height: 1.05; color: var(--brand-black); white-space: nowrap; }
  .card__contact li { display: flex; align-items: flex-start; gap: 14px; margin-bottom: 7px; }
  .card__contact svg { width: 20px; height: 20px; flex: none; }
  .card__contact span { padding-top: 3px; }

  .card--back .card__brand { left: 44px; top: 140px; }
  .card__social { position: absolute; left: 0; top: 330px; width: 228px; height: 28px; }
  .card__handle { position: absolute; left: 0; top: 364px; width: 228px; text-align: center; font-family: var(--display); font-size: 12px; color: var(--paper); }
</style>
</head>
<body>

<svg class="icon-defs" aria-hidden="true">
  <symbol id="icon-phone" viewBox="0 0 20 20"><circle cx="10" cy="10" r="10" fill="#000"/><path d="M6 7.5c0-1.5 8-1.5 8 0v1.2h-2V7.8H8v.9H6zM7 10h6l1 3.5H6z" fill="#fbee3f"/></symbol>
  <symbol id="icon-mail" viewBox="0 0 20 20"><circle cx="10" cy="10" r="10" fill="#000"/><rect x="5.5" y="6.8" width="9" height="6.4" fill="#fbee3f"/><path d="M5.5 6.8l4.5 3.6 4.5-3.6" fill="none" stroke="#000" stroke-width=".9"/></symbol>
  <symbol id="icon-web" viewBox="0 0 20 20"><circle cx="10" cy="10" r="10" fill="#000"/><g fill="none" stroke="#fbee3f" stroke-width="1"><circle cx="10" cy="10" r="4.6"/><ellipse cx="10" cy="10" rx="2" ry="4.6"/><path d="M5.4 10h9.2"/></g></symbol>
  <symbol id="icon-home" viewBox="0 0 20 20"><circle cx="10" cy="10" r="10" fill="#000"/><path d="M10 4.8l5 4.4h-1.5v5.2h-2.4v-3h-2.2v3H6.5V9.2H5z" fill="#fbee3f"/></symbol>
</svg>

<article class="letterhead">
  <svg class="wordmark letterhead__brand" width="202" height="80" viewBox="0 0 202 80">
    <text x="0" y="70" font-size="86" textLength="202" lengthAdjust="spacingAndGlyphs" fill="#000">TARVON</text>
  </svg>
  <ul class="letterhead__contact">
    <li><span>123 456 7890</span><svg><use href="#icon-phone"/></svg></li>
    <li><span>email@domainname.com</span><svg><use href="#icon-mail"/></svg></li>
    <li><span>www.webaddress.com</span><svg><use href="#icon-web"/></svg></li>
    <li><span>48 Larkmoor Ct<br>Brenford, Ohio(OH), ZIP CODE 45210</span><svg><use href="#icon-home"/></svg></li>
  </ul>

  <p class="letter__label letter__salutation">Iorem Ipsum</p>

  <div class="letter__body">
    <p>Lorem ipsum dolor sit amet, consectetur adipiscing elit. Sed a augue eros. Sed sed porttitor diam, sed placerat neque. Phasellus pretium felis orci, vitae tincidunt mauris vulputate in. Cras sodales eget diam at viverra. Nulla quis mi lobortis libero luctus posuere. In non tortor vitae odio feugiat tristique. Sed semper tortor et consectetur suscipit. Donec nisl sapien, ullamcorper eget sagittis vel, iaculis in mi. Donec efficitur nulla in turpis placerat, at molestie neque tincidunt. Vestibulum luctus tincidunt elit, a aliquet erat convallis vel.</p>
    <p>Fusce lacinia condimentum quam nec venenatis. Phasellus tristique, dolor non cursus rutrum, mi dolor convallis ipsum, vel gravida nulla mauris elementum diam. Praesent ut facilisis arcu. Morbi imperdiet eu urna venenatis eleifend. Donec quis risus orci. Nullam elementum velit nisi, a consequat risus varius vitae. Vestibulum at ipsum dolor. Phasellus mattis pellentesque consequat. Phasellus feugiat magna lorem, sed bibendum libero facilisis et. Proin cursus elit eu neque fringilla, sed fermentum diam consectetur. Donec molestie sed orci sit amet iaculis. Fusce molestie vel massa vel tempus. Aliquam erat volutpat. Suspendisse ut orci quam. Duis tristique hendrerit nisi eu laoreet. Vivamus vulputate, ante in aliquet mollis, metus erat tincidunt sem, at feugiat velit massa id lectus.</p>
    <p>Proin ullamcorper, orci eget pulvinar lacinia, nulla mi scelerisque nisl, eu porta lorem lorem sit amet nisi. Lorem ipsum dolor sit amet, consectetur adipiscing elit. Praesent felis nisi, hendrerit ultricies enim eu, ultrices pellentesque felis. Nunc rutrum vitae arcu vel vehicula. Phasellus fringilla velit quis lectus eleifend, eu mollis metus pulvinar. Nam eget ex luctus, fringilla magna sit amet, condimentum purus. Cras vitae erat rhoncus, porta nisi vel, interdum magna. Vivamus at nibh ullamcorper leo tempor malesuada sed in nibh. Cras finibus felis id aliquet tincidunt.</p>
    <p>Nunc vulputate vehicula dictum. Aliquam pretium eros sed leo aliquam, in euismod neque aliquam. Aliquam fringilla sem in dolor tempor luctus. Proin posuere, lacus vitae mollis efficitur, erat quam mollis nisi, vel mattis neque dui ut ipsum. Mauris in lacus diam. Integer odio lacus, lobortis a massa id, tempus molestie felis. Maecenas ornare pretium felis. Nulla facilisi. Nulla mattis a turpis mattis semper. Duis semper odio accumsan viverra pellentesque. Integer egestas tempor dolor, a aliquet lacus eleifend ut. Vestibulum eu vulputate justo. Donec egestas mollis ante id eleifend. Vivamus consectetur dapibus augue, quis iaculis magna pulvinar sit amet.</p>
    <p>Aliquam erat volutpat. Morbi ac imperdiet mi, quis feugiat ante. Proin sodales porttitor odio quis faucibus. Morbi vitae luctus mauris. Praesent eu suscipit arcu. Quisque euismod, dolor ac aliquam dapibus, tellus tellus maximus metus, at sollicitudin nisl risus in nibh. Aliquam ut lectus est. Integer varius vulputate gravida. Aenean sit amet magna non arcu lobortis congue. Nullam ac quam magna.</p>
  </div>

  <p class="letter__label letter__signoff">Iorem Ipsum</p>

  <svg class="letterhead__footer" viewBox="0 0 598 54" aria-hidden="true">
    <rect x="0" y="21" width="208" height="7" fill="#000"/>
    <rect x="0" y="33" width="206" height="6" fill="#000"/>
    <rect x="0" y="45" width="205" height="9" fill="#000"/>
    <path d="M210 54 C210 20 230 0 265 0 H598 V54 Z" fill="#fbee3f"/>
  </svg>
</article>

<section class="card card--front">
  <svg class="card__shape" width="228" height="399" viewBox="0 0 228 399" aria-hidden="true">
    <path d="M0 0 H228 V212 C150 204 70 210 0 220 Z" fill="#000"/>
    <path d="M0 166 C 30 146 70 140 120 140 H228 V152 H122 C 72 152 30 160 0 180 Z" fill="#fff"/>
  </svg>
  <svg class="wordmark card__brand" width="150" height="66" viewBox="0 0 150 66">
    <text x="0" y="58" font-size="72" textLength="150" lengthAdjust="spacingAndGlyphs" fill="#fbee3f">TARVON</text>
  </svg>
  <div class="card__person">
    <div class="card__name">MARCUS HALE</div>
    <div class="card__role">Owner</div>
  </div>
  <ul class="card__contact">
    <li><svg><use href="#icon-phone"/></svg><span>123 456 7890</span></li>
    <li><svg><use href="#icon-mail"/></svg><span>email@domainname.com</span></li>
    <li><svg><use href="#icon-web"/></svg><span>www.webaddress.com</span></li>
    <li><svg><use href="#icon-home"/></svg><span>48 Larkmoor Ct<br>Brenford, Ohio(OH)<br>ZIP CODE 45210</span></li>
  </ul>
</section>

<section class="card card--back">
  <svg class="wordmark card__brand" width="140" height="72" viewBox="0 0 140 72">
    <text x="0" y="64" font-size="80" textLength="140" lengthAdjust="spacingAndGlyphs" fill="#fbee3f">TARVON</text>
  </svg>
  <svg class="card__social" viewBox="0 0 228 28" aria-hidden="true">
    <g stroke="#fff" stroke-width="2"><line x1="0" y1="14" x2="44" y2="14"/><line x1="180" y1="14" x2="228" y2="14"/></g>
    <g fill="none" stroke="#fbee3f" stroke-width="2">
      <circle cx="61" cy="14" r="12"/><circle cx="96" cy="14" r="12"/><circle cx="129" cy="14" r="12"/><circle cx="163" cy="14" r="12"/>
    </g>
  </svg>
  <div class="card__handle">@username</div>
</section>

</body>
</html>
```